Asia based real estate financing firm needs and AWESOME design for a biz card -Harbor Lending Circle

Looking for a stylish, & corporate-looking business card for a real estate financing brokerage firm in Asia, offering global mortgage loans. I uploaded our current logos. We would like to add a splash of color (perhaps the house icon) or any other suggestions are open. For the winning designer, we have a lot of work! Thanks and best of luck!

Target Market(s)

Real estate investors globally. We want to look more like a BANK and NOT a real estate company. Please don't play up on a "house" design.

Industry/Entity Type

Banking

Contact Information for Business Card

Harbor Lending Circle
Peter Wilks
Co-Founder | Partner

14 Cassia Lane, Suite 310
Singapore 047219
www.hlc-example.asia
peterwilks@hlc-example.asia
+65 555-0142
WeChat: peterwilks

Colors

Designer to choose colors to be used in the design.

Requirements
Must have
• Must have the standard business requirements for a card; name, address, email, etc
• Can be horizontal or vertical.
Nice to have
• It would be great to see some sort of variation to the logo with a pop of color. Red is good as we're in Asia, however, other options work as well.
• Our tag line is - Borderless mortgages. It doesn't have to be on the card but might be nice.
• I'd like to start seeing our tagline within the cards as well. - Borderless mortgages.
• Also, please add our location. The location for this card is Singapore so perhaps it can be highlighted or emphasised in some way.
• Singapore | Hong Kong | Shanghai | Manila
• As we will soon open an office in Shanghai, having an option for both languages would be great.
Should not have
• I'm exceited and open to your creativity ... knock it out of the park!

```html
<!DOCTYPE html>
<html lang="en">
<head>
<meta charset="utf-8">
<title>Harbor Lending Circle — Business Card</title>
<link rel="stylesheet" href="https://fonts.googleapis.com/css2?family=Libre+Baskerville:wght@400;700&display=swap">
<style>
  :root {
    --backdrop: #2a2c30;
    --card-dark: #0b0b0c;
    --card-light: #ffffff;
    --ink-dark: #1a1a1a;
    --ink-light: #f4f4f4;
    --accent-red: #c8262c;
    --accent-blue: #233f9e;
    --serif: "Libre Baskerville", Georgia, serif;
  }
  html, body {
    margin: 0;
    width: 1200px;
    height: 900px;
    overflow: hidden;
    background: var(--backdrop);
    font-family: var(--serif);
  }
  .stage {
    position: relative;
    width: 1200px;
    height: 900px;
  }
  .card {
    position: absolute;
    top: 307px;
    width: 500px;
    height: 286px;
    border-radius: 26px;
    overflow: hidden;
    box-shadow: 0 14px 34px rgba(0,0,0,.45);
  }
  .card--front { left: 70px; background: var(--card-dark); color: var(--ink-light); }
  .card--back  { left: 630px; background: var(--card-light); color: var(--ink-dark); }

  .bar { position: absolute; height: 12px; }
  .bar--red { background: var(--accent-red); }
  .bar--blue { background: var(--accent-blue); }

  /* front */
  .card--front .bar--blue { left: 0; top: 62px; width: 96px; }
  .card--front .bar--red { right: 0; top: 212px; width: 96px; }
  .front-name {
    position: absolute;
    left: 0; right: 0; top: 98px;
    margin: 0;
    text-align: center;
    font-size: 30px;
    line-height: 1.25;
    letter-spacing: .04em;
    color: var(--ink-light);
  }
  .front-name small {
    display: block;
    margin-top: 12px;
    font-size: 12px;
    line-height: 1.4;
    letter-spacing: .32em;
    text-transform: uppercase;
  }

  /* back */
  .card--back .bar--red { left: 0; top: 82px; width: 120px; }
  .card--back .bar--blue { right: 0; top: 196px; width: 140px; }
  .person { position: absolute; left: 26px; top: 22px; }
  .person-name { font-weight: 700; font-size: 12px; letter-spacing: .05em; text-transform: uppercase; margin: 0; }
  .person-title { font-size: 11px; margin: 3px 0 0; }
  .back-name {
    position: absolute;
    left: 0; right: 0; top: 154px;
    margin: 0;
    text-align: center;
    font-size: 19px;
    line-height: 1.2;
    letter-spacing: .04em;
  }
  .contact { position: absolute; font-size: 11px; line-height: 1.5; margin: 0; }
  .contact--left { left: 26px; top: 108px; }
  .contact--right { right: 26px; top: 108px; text-align: right; }
  .contact--address { right: 26px; bottom: 22px; text-align: right; }
</style>
</head>
<body>
<main class="stage">
  <section class="card card--front" aria-label="Card front">
    <span class="bar bar--blue"></span>
    <p class="front-name">Harbor<br>Lending Circle<small>Borderless mortgages</small></p>
    <span class="bar bar--red"></span>
  </section>

  <section class="card card--back" aria-label="Card back">
    <div class="person">
      <p class="person-name">Peter Wilks</p>
      <p class="person-title">Co-Founder | Partner</p>
    </div>
    <span class="bar bar--red"></span>
    <p class="contact contact--left">Ph: +65 555-0142<br>WeChat: peterwilks</p>
    <p class="contact contact--right">www.hlc-example.asia<br>peterwilks@hlc-example.asia</p>
    <p class="back-name">Harbor Lending Circle</p>
    <span class="bar bar--blue"></span>
    <p class="contact contact--address">14 Cassia Lane<br>Suite 310, Singapore 047219</p>
  </section>
</main>
</body>
</html>
```